automatic Real Estate Sales Brochure

Print-out of 3 to 8 pages automatically on a color inkjet printer. Page size A4
All details for my Real Estate Sales Design Project are in attached file.
Here some points:
We have abound 100 real estate objects for sale (houses, flats and pieces of land).
For each item, our system creates automatically a sales documentation, which we print out and hand to the potential buyers after they've visited the object or send it by mail upon request in form of a pdf.
This document should be of 3 to maximum 8 pages.
It should be of a modern design and invite the client to read it.
The information should be clear and quick to find.
If the global look could somehow relate to the look of our web site www.velorancasa.ch, that would be nice.
The company data is there for legal reasons, but it is the agent's phone and mail that the clients should use for contact.
The photos should be of big size (2 by page?) without being distorted nor cut.
Optionally, to save ink and pages, maybe only the first 3-4 photos full size and the rest smaller?

Target Market(s)

will be printed or sent as PDF "on the fly", meaning no pre-printing at a print shop!

Industry/Entity Type

Real Estate

Font styles to use
Sans Serif

Requirements
Must have
• see details in attached file
Should not have
• no edge-to-edge printing
• no double-page printing (A3)

```html
<!DOCTYPE html>
<html lang="fr">
<head>
<meta charset="utf-8">
<title>Veloranca – Brochure de vente</title>
<link href="https://fonts.googleapis.com/css2?family=Lato:wght@300;400;700;900&family=Michroma&family=Roboto+Condensed:wght@400;700&display=swap" rel="stylesheet">
<style>
:root{
  --board:#4a7194;
  --red:#e8070c;
  --grey:#7b7c7e;
  --dark:#3d3d3f;
  --ink:#2a2a2a;
  --paper:#ffffff;
  --line:#9a9a9a;
}
*{box-sizing:border-box;margin:0;padding:0}
html,body{width:1200px;height:1200px;overflow:hidden;background:var(--board)}
body{position:relative;font-family:"Lato",sans-serif;color:var(--ink)}
.page{position:absolute;width:329px;height:462px;background:var(--paper);overflow:hidden}
.abs{position:absolute}
.photo{position:absolute}
.brand{font-family:"Lato",sans-serif;font-weight:900;color:var(--red);letter-spacing:.2px}
.date{position:absolute;font-family:"Roboto Condensed",sans-serif;font-weight:700;font-size:6.5px;color:var(--ink)}
.heading{position:absolute;font-family:"Roboto Condensed",sans-serif;font-weight:700;font-size:8.5px;color:var(--red);display:flex;align-items:center;gap:4px}
.heading::after{content:"";display:block;height:0;border-top:.6px solid var(--line);width:var(--rule,60px)}
.small{font-size:4.6px;line-height:6.2px;color:#333}
.small p{margin-bottom:4.4px}

/* page 1 */
.cover{left:53px;top:119px;border:4px solid var(--red)}
.cover .photo{left:0;top:0;width:321px;height:268px;background:linear-gradient(180deg,#6fa6e6 0%,#a9c9ec 30%,#5d8a3c 48%,#3f6f2a 75%,#6a9a3a 100%)}
.cover .band{left:0;top:268px;width:321px;height:4px;background:var(--dark)}
.cover .band i{position:absolute;left:104px;top:0;width:106px;height:4px;background:var(--red)}
.cover .brand{left:0;width:321px;top:290px;text-align:center;font-size:21px}
.cover .tagline{left:0;width:321px;top:320px;text-align:center;font-size:12.5px;color:#444}
.cover .titlebox{left:17px;top:351px;width:288px;height:78px;border:1px solid #555;text-align:center}
.cover .t1{margin-top:12px;font-family:"Michroma",sans-serif;font-size:14px;color:var(--red);letter-spacing:.5px}
.cover .t2{font-family:"Lato",sans-serif;font-weight:400;font-size:27px;color:var(--ink);line-height:30px;letter-spacing:.5px}
.cover .url{left:76px;top:421px;width:138px;height:16px;background:var(--dark);color:#fff;font-size:10px;letter-spacing:1.6px;text-align:center;line-height:16px}

/* page 2 */
.desc{left:417px;top:119px}
.desc .header{left:0;top:0;width:329px;height:104px;background:var(--grey)}
.desc .frame{left:0;top:104px;width:329px;height:358px;border:4px solid var(--red);border-top:none}
.desc .contact{left:37px;top:23px;color:#fff;font-size:7.6px;line-height:9.6px}
.desc .contact .name{color:var(--red);font-style:italic;font-weight:700}
.desc .contact li{list-style:none;display:flex;align-items:center;gap:4px}
.desc .contact li b{display:inline-block;width:5px;height:5px;border-radius:50%;background:var(--red)}
.desc .objtitle{left:37px;top:68px;color:#fff;font-weight:700;font-size:7.8px;line-height:11.5px}
.desc .agent{left:229px;top:11px;width:58px;height:78px;border:2px solid #fff;background:linear-gradient(180deg,#d9d9d9,#9d9d9d)}
.desc .brand{right:40px;top:127px;font-size:13px}
.desc .heading{left:24px;top:138px;--rule:90px}
.desc .small{left:24px;top:153px;width:287px}
.desc .photo{left:21px;top:275px;width:288px;height:168px;background:linear-gradient(90deg,#f6ead0 0%,#efe1bd 40%,#4a3a30 42%,#2b2421 100%)}
.desc .photo::after{content:"";position:absolute;left:0;bottom:0;width:100%;height:38%;background:linear-gradient(180deg,#c98d45,#b57632)}
.desc .date{left:24px;top:449px}

/* page 3 */
.facts{left:776px;top:119px}
.facts .brand{right:62px;top:13px;font-size:13px}
.facts .heading.s1{left:34px;top:44px;--rule:150px}
.facts .sit{left:34px;top:56px;width:258px;font-size:4.6px;line-height:6px}
.facts .heading.s2{left:34px;top:82px;--rule:100px}
.facts table{position:absolute;left:34px;top:99px;width:256px;border-collapse:separate;border-spacing:0;border:1px solid #555;border-radius:3px;font-size:4.6px}
.facts td{padding:3px 3px;border-right:.6px solid #999;border-bottom:.6px solid #999;height:16px}
.facts td:last-child{border-right:none}
.facts tr:last-child td{border-bottom:none}
.facts td em{font-style:normal;color:var(--red);font-weight:700}
.facts td.dash{text-align:center;color:var(--red);font-weight:900}
.facts .heading.s3{left:34px;top:159px;--rule:100px}
.facts .carac{left:34px;top:175px;width:256px;height:70px;border:1px solid #555;border-radius:4px;display:flex;font-size:4.6px}
.facts .col{flex:1;padding:4px 3px}
.facts .col+.col{border-left:1px solid #555;margin:3px 0}
.facts .col div{height:12.4px;display:flex;align-items:center;gap:3px;padding-left:3px}
.facts .col div:nth-child(even){background:#ececec}
.facts .col div em{font-style:normal;font-weight:700;color:var(--red)}
.facts .col svg{width:5px;height:5px;flex:none}
.facts .photo{left:0;top:267px;width:329px;height:152px;background:linear-gradient(180deg,#c9d6e2 0%,#e4edf2 45%,#a86f33 68%,#8e5824 100%)}
.facts .roundframe{left:22px;top:400px;width:285px;height:38px;border:1px solid #555;border-top:none;border-radius:0 0 7px 7px}
.facts .date{left:40px;top:451px}

/* page 4 & 5 */
.gallery{top:656px}
.g1{left:249px}
.g2{left:667px}
.gallery .brand{left:17px;top:12px;font-size:13px;z-index:2}
.g1 .p1{left:6px;top:6px;width:318px;height:235px;background:linear-gradient(90deg,#eeeae2 0%,#dcd6cb 35%,#f1f1ef 36%,#e2e2e0 100%)}
.g1 .p2{left:6px;top:247px;width:153px;height:209px;background:linear-gradient(180deg,#eef0f2 0%,#d9dcdf 60%,#b67a3a 80%,#a26a2f 100%)}
.g1 .p3{left:165px;top:247px;width:159px;height:209px;background:linear-gradient(180deg,#f0f1f1 0%,#c8d9b7 35%,#eeeeee 55%,#b67a3a 72%,#9a6129 100%)}
.g1 .tag{left:0;top:437px;width:115px;height:17px;background:var(--red)}
.g1 .date{left:18px;top:442px;color:#fff}
.g2 .corner{left:0;top:0}
.g2 .p1{left:10px;top:6px;width:307px;height:278px;background:linear-gradient(180deg,#eaebed 0%,#d8d2c8 45%,#b47838 60%,#97602a 100%)}
.g2 .p2{left:10px;top:294px;width:307px;height:159px;background:linear-gradient(90deg,#f2f2f2 0%,#e6e8ea 60%,#d4d8dc 100%)}
.g2 .date{left:32px;top:448px}
</style>
</head>
<body>

<!-- Page 1 : cover -->
<section class="page cover">
  <div class="photo" role="img" aria-label="Photo du jardin arboré devant l'immeuble, ciel bleu"></div>
  <div class="abs band"><i></i></div>
  <div class="abs brand">Veloranca</div>
  <div class="abs tagline">Spécialiste Romand De Vente Immobilière</div>
  <div class="abs titlebox">
    <div class="t1">LUMINEUX 4.5 DE 100M2</div>
    <div class="t2">IDÉALEMENT SITUÉ</div>
  </div>
  <div class="abs url">www.velorancasa.ch</div>
</section>

<!-- Page 2 : description -->
<section class="page desc">
  <div class="abs header"></div>
  <svg class="abs" style="left:0;top:100px" width="329" height="12" viewBox="0 0 329 12"><polygon points="22,4 180,4 172,9 22,9" fill="var(--red)"/><polygon points="180,4 329,4 329,9 172,9" fill="var(--grey)" opacity="0"/></svg>
  <div class="abs frame"></div>
  <ul class="abs contact">
    <li class="name"><b></b>Nadia Morel</li>
    <li><b></b>morel@velorancasa.ch</li>
    <li>
      <svg width="6" height="6" viewBox="0 0 10 10"><path d="M2 1l2 0 1 2.5-1.3 1a6 6 0 0 0 2.8 2.8l1-1.3L10 7v2c0 .6-.5 1-1 1A9 9 0 0 1 1 2c0-.5.4-1 1-1z" fill="var(--red)"/></svg>077 000 12 34
    </li>
  </ul>
  <div class="abs objtitle">Lumineux 4.5 de 100m2 Idéalement Situé<br>Chemin des Aulnes ,1200 Genève</div>
  <div class="abs agent" role="img" aria-label="Portrait de la conseillère"></div>
  <div class="abs brand">Veloranca</div>
  <div class="heading">DESCRIPTION</div>
  <div class="abs small">
    <p>Venez visiter sans tarder ce bel appartement situé dans un environnement calme et vert tout en étant proche du centre-ville et de toutes les commodités. Il profite de beaux volumes et de pièces de vie très lumineuses. Au 1er étage d'une copropriété soignée, c'est le bien idéal pour un couple ou une famille.</p>
    <p>Cet appartement pourrait aussi convenir comme investissement pour un client souhaitant le louer.</p>
    <p>Il est en bon état d'entretien et se réjouit d'accueillir ses nouveaux propriétaires !</p>
    <p>Il se distribue ainsi :</p>
    <p>Une entrée avec armoire encastrée dessert de part et d'autre la partie jour et la partie nuit. La spacieuse pièce de vie se compose d'une cuisine ouverte entièrement équipée et aménagée s'ouvrant sur le séjour. Il profite d'une exposition optimale. Du séjour, vous avez accès à un agréable balcon qui offre une belle vue dégagée sur un environnement verdoyant.</p>
    <p>La partie nuit offre trois belles chambres, une salle de bains avec baignoire, lavabo, wc ainsi qu'un wc visiteurs.</p>
    <p>Deux places de parc intérieures en sus s'ajoutent à ce bel appartement !</p>
    <p>N'hésitez pas, contactez-moi pour plus d'informations et pour une visite !</p>
  </div>
  <div class="photo" role="img" aria-label="Photo d'une chambre avec grande armoire à portes coulissantes et parquet"></div>
  <div class="date">jeudi 28 septembre 2017</div>
</section>

<!-- Page 3 : situation & caractéristiques -->
<section class="page facts">
  <svg class="abs" style="left:0;top:0" width="329" height="462" viewBox="0 0 329 462">
    <polygon points="0,0 155,0 140,14 14,14 14,160 0,175" fill="var(--red)"/>
    <polygon points="329,310 329,405 300,439 300,330" fill="var(--red)"/>
    <polygon points="230,449 329,449 329,462 240,462" fill="var(--red)"/>
  </svg>
  <div class="abs brand">Veloranca</div>
  <div class="heading s1">SITUATION</div>
  <div class="abs sit">Cet appartement a l'avantage de se situer proche de toutes les commodités, à 3 minutes du Collège des Vergers, à 1 minute de l'arrêt de bus et à 3 minutes des axes autoroutiers. Vous rejoindrez le centre-ville en 7 minutes. Des atouts que vous saurez apprécier.</div>
  <div class="heading s2">APPARTEMENT, MAISON, TERRAIN</div>
  <table>
    <tr><td><em>CHF</em> ------------- 910'000</td><td><em>SURFACE HABITABLE</em> -- 100m2</td><td><em>SURFACE PARCELLE</em> -- 1'000m2</td></tr>
    <tr><td><em>PIÈCES</em> ------------ 4.5</td><td><em>ANNÉE</em> ---------------- 1994</td><td class="dash">–</td></tr>
    <tr><td><em>DISPONIBLE</em> ----- 1.1.2018</td><td><em>ÉTAT</em> ------------- BON ÉTAT</td><td class="dash">–</td></tr>
  </table>
  <div class="heading s3">CARACTÉRISTIQUES</div>
  <div class="abs carac">
    <div class="col">
      <div><svg viewBox="0 0 10 10"><circle cx="5" cy="5" r="4.2" fill="none" stroke="#333" stroke-width="1.2"/><path d="M3 5.2l1.5 1.5L7.2 3.8" fill="none" stroke="#333" stroke-width="1.2"/></svg><em>ETAGE</em> : 1er étage</div>
      <div><svg viewBox="0 0 10 10"><circle cx="5" cy="5" r="4.2" fill="none" stroke="#333" stroke-width="1.2"/><path d="M3 5.2l1.5 1.5L7.2 3.8" fill="none" stroke="#333" stroke-width="1.2"/></svg><em>VUE</em> : Vue dégagée sur le parc</div>
      <div><svg viewBox="0 0 10 10"><circle cx="5" cy="5" r="4.2" fill="none" stroke="#333" stroke-width="1.2"/><path d="M3 5.2l1.5 1.5L7.2 3.8" fill="none" stroke="#333" stroke-width="1.2"/></svg><em>COMMERCES</em> : à Proximité Immédiate</div>
      <div><svg viewBox="0 0 10 10"><circle cx="5" cy="5" r="4.2" fill="none" stroke="#333" stroke-width="1.2"/><path d="M3 5.2l1.5 1.5L7.2 3.8" fill="none" stroke="#333" stroke-width="1.2"/></svg><em>ECOLES</em> : Collège des Vergers</div>
      <div><svg viewBox="0 0 10 10"><circle cx="5" cy="5" r="4.2" fill="none" stroke="#333" stroke-width="1.2"/><path d="M3 5.2l1.5 1.5L7.2 3.8" fill="none" stroke="#333" stroke-width="1.2"/></svg><em>TRANSPORT PUBLIC</em> : à 5 minutes à pied</div>
    </div>
    <div class="col">
      <div><svg viewBox="0 0 10 10"><circle cx="5" cy="5" r="4.2" fill="none" stroke="#333" stroke-width="1.2"/><path d="M3 5.2l1.5 1.5L7.2 3.8" fill="none" stroke="#333" stroke-width="1.2"/></svg><em>CHAUFFAGE</em> : Mazout / au sol</div>
      <div><svg viewBox="0 0 10 10"><circle cx="5" cy="5" r="4.2" fill="none" stroke="#333" stroke-width="1.2"/><path d="M3 5.2l1.5 1.5L7.2 3.8" fill="none" stroke="#333" stroke-width="1.2"/></svg><em>CAVE</em> : Oui</div>
      <div><svg viewBox="0 0 10 10"><circle cx="5" cy="5" r="4.2" fill="none" stroke="#333" stroke-width="1.2"/><path d="M3 5.2l1.5 1.5L7.2 3.8" fill="none" stroke="#333" stroke-width="1.2"/></svg><em>GARAGE</em> : 2 places de parc intérieures</div>
      <div><svg viewBox="0 0 10 10"><circle cx="5" cy="5" r="4.2" fill="none" stroke="#333" stroke-width="1.2"/><path d="M3 5.2l1.5 1.5L7.2 3.8" fill="none" stroke="#333" stroke-width="1.2"/></svg><em>BALCON</em> : Oui</div>
      <div><svg viewBox="0 0 10 10"><circle cx="5" cy="5" r="4.2" fill="none" stroke="#333" stroke-width="1.2"/><path d="M3 5.2l1.5 1.5L7.2 3.8" fill="none" stroke="#333" stroke-width="1.2"/></svg><em>ASCENSEUR</em> : Oui</div>
    </div>
  </div>
  <div class="abs roundframe"></div>
  <div class="photo" role="img" aria-label="Photo du séjour lumineux avec baies vitrées et parquet"></div>
  <div class="date">jeudi 28 septembre 2017</div>
</section>

<!-- Page 4 : galerie -->
<section class="page gallery g1">
  <div class="abs brand">Veloranca</div>
  <div class="photo p1" role="img" aria-label="Photo de la cuisine et de l'entrée avec armoire encastrée"></div>
  <div class="photo p2" role="img" aria-label="Photo du couloir menant aux chambres"></div>
  <div class="photo p3" role="img" aria-label="Photo d'une chambre avec fenêtres sur la verdure"></div>
  <svg class="abs tag" viewBox="0 0 115 17" width="115" height="17"><polygon points="0,0 115,0 108,17 0,17" fill="var(--red)"/></svg>
  <div class="date">jeudi 28 septembre 2017</div>
</section>

<!-- Page 5 : galerie -->
<section class="page gallery g2">
  <svg class="abs corner" width="329" height="462" viewBox="0 0 329 462">
    <polygon points="196,0 329,0 329,110 317,95 317,14 210,14" fill="var(--dark)"/>
    <polygon points="0,395 0,462 140,462 130,452 10,452 10,405" fill="var(--red)"/>
  </svg>
  <div class="abs brand">Veloranca</div>
  <div class="photo p1" role="img" aria-label="Photo de la pièce de vie avec cuisine ouverte et porte-fenêtre"></div>
  <div class="photo p2" role="img" aria-label="Photo de la salle de bains avec lavabo, wc et baignoire"></div>
  <div class="date">jeudi 28 septembre 2017</div>
</section>

</body>
</html>
```